Banner Ad Design Project

I require banner ad designs with the below wording.

1. Join Today and Make Money Tomorrow. Unlimited Income. Click Here Now

2. I lost my job. Now I Make Over $5,000 Per Week From Home. You Can Too. Free Info, Apply Now

I require sizes: 300x250 and 728x90 and 468x60 and 120x240

The design should communicate legitimate, accredited, online business.

Industry/Entity Type

Business

Requirements
Should not have
• Creative attributes to avoid*
Phone numbers in creative
Creative with no click buttons
Interactive creative
Brand messaging with no call to action
Creative with long looping times

```html
<!DOCTYPE html>
<html lang="en">
<head>
<meta charset="utf-8">
<title>Join Today Banner</title>
<link rel="stylesheet" href="https://fonts.googleapis.com/css2?family=Source+Sans+3:wght@600;700;800&family=Yellowtail&display=swap">
<style>
  :root {
    --page-bg: #2b2b2b;
    --banner-blue-light: #4a7dbd;
    --banner-blue: #3765a3;
    --banner-blue-dark: #24497f;
    --banner-border: #0e1a2c;
    --headline-white: #ffffff;
    --headline-navy: #1f2f4a;
    --button-top: #c43bb8;
    --button-bottom: #8e1c86;
    --button-edge: #6a1264;
    --photo-light: #dbe8f5;
    --photo-mid: #a9c3e0;
  }
  * { margin: 0; padding: 0; box-sizing: border-box; }
  html, body {
    width: 1200px;
    height: 900px;
    overflow: hidden;
    background: var(--page-bg);
  }
  .banner {
    position: absolute;
    left: 300px;
    top: 200px;
    width: 600px;
    height: 500px;
    overflow: hidden;
    border: 2px solid var(--banner-border);
    background: radial-gradient(ellipse at 60% 35%, var(--banner-blue-light) 0%, var(--banner-blue) 55%, var(--banner-blue-dark) 100%);
    font-family: "Source Sans 3", Arial, sans-serif;
  }
  .banner__photo {
    position: absolute;
    left: 12px;
    top: 12px;
    width: 250px;
    height: 488px;
    border-radius: 110px 110px 0 0;
    background: linear-gradient(180deg, var(--photo-mid) 0%, var(--photo-light) 60%, #eef1f4 100%);
  }
  .headline {
    position: absolute;
    left: 288px;
    line-height: 1;
    white-space: nowrap;
  }
  .headline--join {
    top: -4px;
    left: 284px;
    font-size: 155px;
    font-weight: 600;
    letter-spacing: -3px;
    color: var(--headline-white);
  }
  .headline--today {
    top: 135px;
    font-size: 62px;
    font-weight: 800;
    color: var(--headline-navy);
  }
  .headline--today .amp {
    color: var(--headline-white);
    margin-left: 20px;
  }
  .headline--money {
    top: 198px;
    font-size: 50px;
    font-weight: 700;
    color: var(--headline-white);
  }
  .headline--tomorrow {
    top: 242px;
    font-size: 52px;
    font-weight: 800;
    color: var(--headline-navy);
  }
  .cta-button {
    position: absolute;
    left: 292px;
    top: 324px;
    width: 272px;
    height: 72px;
    border-radius: 8px;
    border: 2px solid var(--button-edge);
    background: linear-gradient(180deg, var(--button-top) 0%, var(--button-bottom) 100%);
    box-shadow: inset 0 2px 0 rgba(255,255,255,0.35), 0 3px 6px rgba(0,0,0,0.3);
    color: var(--headline-white);
    font-size: 29px;
    font-weight: 700;
    text-align: center;
    line-height: 68px;
    white-space: nowrap;
  }
  .tagline {
    position: absolute;
    left: 290px;
    top: 424px;
    width: 272px;
    text-align: center;
    font-family: "Yellowtail", cursive;
    font-size: 38px;
    line-height: 50px;
    color: var(--headline-white);
    white-space: nowrap;
  }
</style>
</head>
<body>
  <div class="banner">
    <div class="banner__photo" role="img" aria-label="Smiling businesswoman in a light blue shirt and white skirt"></div>
    <div class="headline headline--join">Join</div>
    <div class="headline headline--today">TODAY<span class="amp">&amp;</span></div>
    <div class="headline headline--money">MAKE MONEY</div>
    <div class="headline headline--tomorrow">TOMORROW</div>
    <div class="cta-button">CLICK HERE NOW</div>
    <div class="tagline">Unlimited Income</div>
  </div>
</body>
</html>
```